Create Stationary from existing logo(s)

We are looking for some assistance in tidying up the stationary that supports our brand. We are an innovative technology company, generally working with larger corporates. We have previously done a little work on brochures etc, but never really pulled it all together with our stationary.
In particular I am looking for:
1. A4 Letter Template for Letter (Microsoft Word 2007 template format)
2. A4 Template for Reports (Microsoft Word 2007 template format). This should include title page, table of contents, subsequent report pages including styles for tables, headings, and text.
3. Business Card Design - we will need to be able to edit the text, so the card should include sample text for name, title, phone number, mobile number, and email address.
4. Presentation Template (Microsoft Powerpoint 2007 template). See attached powerpoint which we quite like, but isn't really a template, and we have don't really use any consistent styles in it. The Powerpoint template needs to have a cover / title page, section break pages, and pages that may contain bullet point text, pictures, or a combination of bullet point text and pictures. We do like our current presentation, which gives some indication of our thinking.
I am attaching a brochure and the powerpoint presentation to give some indication of current materials. We are happy with the main concepts behind the brochure, and would not really be looking to change the key concepts unless you have a compelling reason. We do like the use of this secondary logo in the stationary related items
I have uploaded an eps file of the logo.

```html
<!DOCTYPE html>
<html lang="en">
<head>
<meta charset="utf-8">
<title>Veltrix Systems – Business Card Concepts</title>
<link href="https://fonts.googleapis.com/css2?family=Source+Sans+3:wght@400;600&display=swap" rel="stylesheet">
<style>
  :root {
    --sheet: #808080;
    --card-white: #f3f3f3;
    --card-edge: #c9c9c9;
    --brand-blue: #114a7c;
    --brand-orange: #f39a1f;
    --text-dark: #3a3a3a;
    --grey-light: #e4e4e4;
    --grey-mid: #b4b4b4;
    --grey-dark: #9c9c9c;
  }
  * { box-sizing: border-box; margin: 0; padding: 0; }
  html, body {
    width: 854px; height: 1200px; overflow: hidden;
    background: var(--sheet);
    font-family: "Source Sans 3", "Myriad Pro", Arial, sans-serif;
  }
  .sheet { position: relative; width: 854px; height: 1200px; }

  .card {
    position: absolute; width: 361px; height: 233px; overflow: hidden;
    background: var(--card-white);
    border: 1px solid var(--card-edge);
  }
  .card--grey {
    background: radial-gradient(ellipse at 50% 48%, var(--grey-light) 0%, var(--grey-mid) 62%, var(--grey-dark) 100%);
    border-color: #a6a6a6;
  }
  .card--blue { background: var(--brand-blue); border-color: var(--brand-blue); }

  /* Wordmark: invented name, one colour, one weight, plain square beside it */
  .wordmark {
    position: absolute; display: flex; align-items: center; gap: 5px;
    font-weight: 600; color: var(--brand-blue); white-space: nowrap;
  }
  .wordmark__square { background: currentColor; flex: none; }
  .wordmark--small { font-size: 15px; }
  .wordmark--small .wordmark__square { width: 12px; height: 12px; }
  .wordmark--centered { left: 50%; top: 50%; transform: translate(-50%, -50%); }

  .wordmark--stacked { align-items: flex-start; gap: 7px; font-size: 27px; line-height: 26px; }
  .wordmark--stacked .wordmark__square { width: 16px; height: 16px; margin-top: 6px; }
  .wordmark__lines { display: flex; flex-direction: column; align-items: flex-end; }
  .wordmark__lines span:last-child { font-size: 20px; line-height: 22px; }
  .wordmark--on-blue { color: var(--brand-orange); }

  /* Area reserved for the brand symbol graphic */
  .brand-graphic { position: absolute; }
  .brand-graphic--blue { background: linear-gradient(160deg, #1a5a91 0%, var(--brand-blue) 70%); }
  .brand-graphic--silver { background: linear-gradient(160deg, #f0f0f0 0%, #b9b9b9 100%); }

  .contact { position: absolute; color: var(--text-dark); }
  .contact__name { font-size: 12.5px; line-height: 14px; color: #222; }
  .contact__title { font-size: 5px; letter-spacing: 0.2px; text-transform: uppercase; margin-bottom: 6px; }
  .contact__line { font-size: 8.5px; line-height: 10.7px; }
  .contact__gap { height: 5px; }
</style>
</head>
<body>
<main class="sheet">

  <!-- Concept 1 -->
  <section class="card card--grey" style="left:29px; top:33px;">
    <div class="wordmark wordmark--small wordmark--centered"><span class="wordmark__square"></span>Veltrix Systems</div>
  </section>
  <section class="card" style="left:474px; top:33px;">
    <div class="wordmark wordmark--small" style="right:16px; top:26px;"><span class="wordmark__square"></span>Veltrix Systems</div>
    <div class="contact" style="left:47px; top:84px;">
      <p class="contact__name">Alex Morgan</p>
      <p class="contact__title">Account Manager</p>
      <p class="contact__line">Level 4, 120 Harbour Street</p>
      <p class="contact__line">Sydney, 2000 Australia</p>
      <p class="contact__line">Phone: +61 2 9100 2741</p>
      <p class="contact__line">Fax:+61 2 9100 5520</p>
      <p class="contact__line">Mobile: +61 2 9100 5520</p>
      <div class="contact__gap"></div>
      <p class="contact__line">alex.morgan@veltrixsystems.com.au</p>
      <p class="contact__line">www.veltrixsystems.com.au</p>
    </div>
  </section>

  <!-- Concept 2 -->
  <section class="card" style="left:34px; top:345px;">
    <div class="brand-graphic brand-graphic--blue" role="img" aria-label="Brand symbol graphic area" style="left:0; top:40px; width:185px; height:193px;"></div>
    <div class="wordmark wordmark--stacked" style="right:16px; top:66px;"><span class="wordmark__square"></span><span class="wordmark__lines"><span>Veltrix</span><span>Systems</span></span></div>
  </section>
  <section class="card" style="left:474px; top:342px;">
    <div class="wordmark wordmark--small" style="left:16px; top:24px;"><span class="wordmark__square"></span>Veltrix Systems</div>
    <div class="brand-graphic brand-graphic--blue" role="img" aria-label="Brand symbol graphic area" style="left:0; top:84px; width:135px; height:149px;"></div>
    <div class="contact" style="left:158px; top:106px;">
      <p class="contact__name">Alex Morgan</p>
      <p class="contact__title">Account Manager</p>
      <p class="contact__line">Level 4, 120 Harbour Street</p>
      <p class="contact__line">Sydney, 2000 Australia</p>
      <p class="contact__line">Phone: +61 2 9100 2741</p>
      <p class="contact__line">Fax:+61 2 9100 5520</p>
      <p class="contact__line">Mobile: +61 2 9100 5520</p>
      <div class="contact__gap"></div>
      <p class="contact__line">alex.morgan@veltrixsystems.com.au</p>
      <p class="contact__line">www.veltrixsystems.com.au</p>
    </div>
  </section>

  <!-- Concept 3 -->
  <section class="card card--grey" style="left:28px; top:628px;">
    <div class="wordmark wordmark--small wordmark--centered"><span class="wordmark__square"></span>Veltrix Systems</div>
  </section>
  <section class="card" style="left:474px; top:627px;">
    <div class="wordmark wordmark--small" style="left:16px; top:24px;"><span class="wordmark__square"></span>Veltrix Systems</div>
    <div class="brand-graphic brand-graphic--blue" role="img" aria-label="Brand symbol graphic area" style="left:0; top:84px; width:135px; height:149px;"></div>
    <div class="contact" style="left:158px; top:106px;">
      <p class="contact__name">Alex Morgan</p>
      <p class="contact__title">Account Manager</p>
      <p class="contact__line">Level 4, 120 Harbour Street</p>
      <p class="contact__line">Sydney, 2000 Australia</p>
      <p class="contact__line">Phone: +61 2 9100 2741</p>
      <p class="contact__line">Fax:+61 2 9100 5520</p>
      <p class="contact__line">Mobile: +61 2 9100 5520</p>
      <div class="contact__gap"></div>
      <p class="contact__line">alex.morgan@veltrixsystems.com.au</p>
      <p class="contact__line">www.veltrixsystems.com.au</p>
    </div>
  </section>

  <!-- Concept 4 -->
  <section class="card card--blue" style="left:34px; top:932px;">
    <div class="brand-graphic brand-graphic--silver" role="img" aria-label="Brand symbol graphic area" style="left:0; top:40px; width:185px; height:193px;"></div>
    <div class="wordmark wordmark--stacked wordmark--on-blue" style="right:16px; top:66px;"><span class="wordmark__square"></span><span class="wordmark__lines"><span>Veltrix</span><span>Systems</span></span></div>
  </section>
  <section class="card" style="left:474px; top:929px;">
    <div class="wordmark wordmark--small" style="left:16px; top:24px;"><span class="wordmark__square"></span>Veltrix Systems</div>
    <div class="brand-graphic brand-graphic--blue" role="img" aria-label="Brand symbol graphic area" style="left:0; top:84px; width:135px; height:149px;"></div>
    <div class="contact" style="left:158px; top:106px;">
      <p class="contact__name">Alex Morgan</p>
      <p class="contact__title">Account Manager</p>
      <p class="contact__line">Level 4, 120 Harbour Street</p>
      <p class="contact__line">Sydney, 2000 Australia</p>
      <p class="contact__line">Phone: +61 2 9100 2741</p>
      <p class="contact__line">Fax:+61 2 9100 5520</p>
      <p class="contact__line">Mobile: +61 2 9100 5520</p>
      <div class="contact__gap"></div>
      <p class="contact__line">alex.morgan@veltrixsystems.com.au</p>
      <p class="contact__line">www.veltrixsystems.com.au</p>
    </div>
  </section>

</main>
</body>
</html>
```